Cosmetic injections clinic needs a fresh looking business card

We need a business card using the supplied logo and color scheme to attract future clients to our clinic. It should be modern and fresh, eye catching and not too busy. Simple and to the point is best. I would like two sided designs with the front indicating address and contact information, and the back in full color with white logo and descriptive information also provided.
Target Market(s)
Clients looking for non surgical beauty enhancements.
Contact Information for Business Card
MeloraSkin
14, 618 Birchmont Way
St. Albert, Alberta
K2P 7W3
Phone: 587-412-6630
Email: info@meloraskin.com
Requirements
Must have
- -Logo supplied with the name and address of the clinic
- -Back of card in full color with white logo with A small line of text indicating both of the following: Anti aging consultants and cosmetic injectables
- Located inside the Voyager Wellness Group

```html
<!DOCTYPE html>
<html lang="en">
<head>
<meta charset="utf-8">
<title>MeloraSkin — Business Card</title>
<link href="https://fonts.googleapis.com/css2?family=Montserrat:wght@300;400;500;600&display=swap" rel="stylesheet">
<style>
  :root {
    --page: #f1e6ee;
    --card-white: #fbfafa;
    --ink-grey: #7c7a80;
    --purple: #7b4fa6;
    --purple-deep: #6a45a0;
    --magenta: #c0438f;
    --teal: #1a9ba8;
    --white: #ffffff;
  }
  * { margin: 0; padding: 0; box-sizing: border-box; }
  html, body {
    width: 1200px;
    height: 1200px;
    overflow: hidden;
    background: var(--page);
    font-family: "Montserrat", sans-serif;
  }
  .sheet {
    position: relative;
    width: 1200px;
    height: 1200px;
  }
  .card {
    position: absolute;
    left: 190px;
    width: 820px;
    height: 468px;
    border-radius: 4px;
    box-shadow: 0 10px 24px rgba(90, 50, 90, 0.12);
  }

  /* Front: contact side */
  .card--front {
    top: 110px;
    background: var(--card-white);
    border-bottom: 3px solid var(--magenta);
  }
  .brand-mark {
    position: absolute;
    left: 70px;
    top: 196px;
    display: flex;
    align-items: center;
    gap: 14px;
  }
  .brand-mark__dot {
    width: 40px;
    height: 40px;
    border-radius: 50%;
    background: var(--purple);
  }
  .brand-mark__name {
    font-size: 38px;
    font-weight: 500;
    color: var(--purple);
    letter-spacing: 0.5px;
  }
  .contact {
    position: absolute;
    left: 420px;
    top: 112px;
  }
  .contact__title {
    font-size: 17px;
    font-weight: 400;
    letter-spacing: 4px;
    color: var(--ink-grey);
    text-transform: uppercase;
    margin-bottom: 36px;
  }
  .contact__row {
    display: flex;
    align-items: flex-start;
    gap: 14px;
    margin-bottom: 22px;
    font-size: 17px;
    font-weight: 400;
    color: var(--ink-grey);
    line-height: 1.25;
  }
  .contact__row--phone { letter-spacing: 2px; font-size: 18px; }
  .contact__icon {
    width: 22px;
    height: 22px;
    flex: none;
    fill: var(--purple);
  }

  /* Back: full colour side */
  .card--back {
    top: 630px;
    background:
      radial-gradient(circle at 100% 0%, rgba(26,155,168,0.95) 0%, rgba(26,155,168,0) 45%),
      radial-gradient(circle at 0% 100%, rgba(192,67,143,0.95) 0%, rgba(192,67,143,0) 50%),
      linear-gradient(135deg, var(--purple) 0%, var(--purple-deep) 55%, #4f4a98 100%);
    border-bottom: 3px solid var(--magenta);
    color: var(--white);
    text-align: center;
  }
  .back-brand {
    position: absolute;
    left: 0;
    right: 0;
    top: 160px;
    display: flex;
    justify-content: center;
    align-items: center;
    gap: 18px;
  }
  .back-brand__dot {
    width: 58px;
    height: 58px;
    border-radius: 50%;
    background: var(--white);
  }
  .back-brand__name {
    font-size: 62px;
    font-weight: 600;
    letter-spacing: 1px;
  }
  .tagline {
    position: absolute;
    left: 0;
    right: 0;
    top: 300px;
    font-size: 19px;
    font-weight: 300;
    letter-spacing: 4px;
    line-height: 1.45;
    text-transform: uppercase;
  }
</style>
</head>
<body>
<main class="sheet">

  <section class="card card--front" aria-label="Business card front">
    <div class="brand-mark">
      <span class="brand-mark__dot"></span>
      <span class="brand-mark__name">MeloraSkin</span>
    </div>

    <div class="contact">
      <p class="contact__title">MeloraSkin</p>

      <p class="contact__row contact__row--phone">
        <svg class="contact__icon" viewBox="0 0 24 24" aria-hidden="true">
          <path d="M6.6 10.8a15.1 15.1 0 0 0 6.6 6.6l2.2-2.2c.3-.3.7-.4 1-.2 1.1.4 2.3.6 3.6.6.6 0 1 .4 1 1V20c0 .6-.4 1-1 1A17 17 0 0 1 3 4c0-.6.4-1 1-1h3.5c.6 0 1 .4 1 1 0 1.3.2 2.5.6 3.6.1.3 0 .7-.2 1z"/>
        </svg>
        587-412-6630
      </p>

      <p class="contact__row">
        <svg class="contact__icon" viewBox="0 0 24 24" aria-hidden="true">
          <path d="M2 5h20v14H2z M3.5 6.5 12 13l8.5-6.5" fill="var(--purple)"/>
          <path d="M3 6l9 7 9-7" fill="none" stroke="#fbfafa" stroke-width="1.6"/>
        </svg>
        info@meloraskin.com
      </p>

      <p class="contact__row">
        <svg class="contact__icon" viewBox="0 0 24 24" aria-hidden="true">
          <path d="M12 2a7 7 0 0 0-7 7c0 5.2 7 13 7 13s7-7.8 7-13a7 7 0 0 0-7-7zm0 9.5A2.5 2.5 0 1 1 12 6.5a2.5 2.5 0 0 1 0 5z"/>
        </svg>
        <span>14, 618 Birchmont Way<br>St. Albert, Alberta, K2P 7W3</span>
      </p>
    </div>
  </section>

  <section class="card card--back" aria-label="Business card back">
    <div class="back-brand">
      <span class="back-brand__dot"></span>
      <span class="back-brand__name">MeloraSkin</span>
    </div>
    <p class="tagline">Anti-Aging Consultants<br>Cosmetic Injectables</p>
  </section>

</main>
</body>
</html>
```